Online travel site needs edgy website design

tripvane is the first Global Business Travel Website that provides the most comprehensive destination information tailored to suit the business traveller.

It is a ‘one click solution’ that offers direct access to all aspects of business travel, including general information on the city, accommodation and transportation options, economic and financial statistics, key business and services contacts, as well as leisure activities, entertainment suggestions, and listings for any personal needs.

Much more than a travel website, tripvane.com eliminates the need to buy multiple travel books or visit scores of websites. Most importantly, it is the only website that will cover such an extensive range of destinations around the world, while also featuring cities where information is really scarce. The user-friendly and consistent format for all destinations will allow the business traveller to easily navigate through more than 100 information pages on any destination.

tripvane will be simple to navigate, intuitive, unique in design, dynamic, and content rich providing a supreme user experience during navigation of the website.

The website will initially be English and is set to expand to more languages in the future.

A beta site with back-end database has been built - and now we need an edgy state of the art graphic design to reskin it.

LOOK & FEEL

Scope
The design of the site should reflect tripvane’s corporate and user centric philosophy with the following elements:

a. tripvane corporate image and branding
b. the promotion of each city destination
c. tripvane being the starting point of travel, while also a partner during travel
d. the subtle but powerful presence of advertising and sponsorship

All the above must derive from the design outline and elements that are going to be used.

Design Guidelines

Innovative and elegant design, minimalism, simplicity that permits the offering of the required information to be delivered in line with the values of Trust, Care, Discovery & Connection.

In addition:

1. The usability, navigation and the informative character of the corporate web site should not be compromised by the design.
2. The over-segmented pages and over-crowded content per page should be avoided.
3. The design should not only guide the user in an inviting way to the information required but also to intrigue them for further navigation.
4. Advertising space should be anticipated in line with the design character and DMQ standard ad sizes.
5. The use of photos / videos should also encouraged.

Key Elements

a. Branding/Logos
Throughout the website branding should be present as a “guarantee seal” for the content accuracy. Corporate logo should be placed on every page while branding should also characterise any content element and/or tool. Appendix contains the current brand guidelines. Should additional sub-logos be required for specific sections, these should be proposed.

b. Fonts
Provided your experience on the website design you are requested to propose alternative font types and sizes always taken into consideration the inviting and user friendly character that the new website should aspire to. The font type that will be proposed must be user friendly in English typography, but also could support other languages in the future.

Given the fact that the majority of the text in the website contains information and listing, the fonts and text layout should not strain and fatigue the reader.

c. SEO
The design should be friendly towards the search engines.

d. Colours
Colour is considered as an integral part of the brand identity. Tripvane.com corporate colours are orange and grey as per the Attached document reference guide.

Different tonalities of the brand colours, or colours in general, should be proposed and applied, guided always by the above described scope of Look & Feel.

e. Section Headings
As presented above, the site’s section headings (refer Overview of the Site.) The principle is to label the content following users’ needs and mindset. However, the label space should be flexible for changes. The labels should facilitate the user to understand the content they host. This is important and should be applied especially to informative content.

Another function that Headings should perform is that of promoting the website’s content, especially when this kind of content will make the user spend more time in the website. This category of Headings should be approached in a more creative and attractive way as to intrigue users to check the content hosted.

f. Icons
Icons are considered necessary in order to provide the user extra help to guide them to reach the information they need quick n’ easy. Icons not only contribute actively to the creation of an attractive look & feel but, most importantly, facilitate navigation and speed up the users’ familiarisation with the website too.

Therefore their design should be eye-catching, comprehensive and dynamic, in accordance to the new site’s colour coding and following the latest trends as these were defined by the look & feel of smart phones.

PIXELHIVE BRIEF REQUIREMENTS
Based on the above, please provide at least two (2) approaches for the following pages – this includes colour palette in line with logo, layout, fonts.

Initial submissions can just address Deliverable 1 & 2 to fine tune design before proceeding further.

Please refer sample screenshots separately attached from raw beta site for content – available for Deliverables 2 -6.

(REFER example sites we like for their creativity: http://www.brindle-studio.example.co.uk/#Background, http://www.rotaclarafestas.example.com.br/, http://pembrookweb.example.co.uk/ )

Deliverable 1: Landing /Home page
- Access log in –
o Free Account or via Workloop/Chatterbox etc
o Membership Access – Login
- How to use the site
- Allowance for video or animation
- Destination Selection
- Blog & Social media links

Deliverable 2: Destination Landing Page / Template
This is essentially a city guide template to be used for all cities throughout the site.

This page clearly depicts the four information sections
1. General
2. Business
3. Leisure
4. Personal

Also this page should include:
- Business News Feed
- Advertising & Sponsorship Spaces (according to DMQ Standards)
- Destination Time, Weather, FX rates (LIVE feeds)
- Tips

Deliverable 3: Follow the above format but show an Internal Content Page – text only with subheadings

Deliverable 4: Follow the above format but show an Internal Content Page – text and photos

Deliverable 5: Follow the above format but show an Internal Content Page – Listing Sections such as Restaurants (this must also include filter categories)

Deliverable 6: Follow the above format but show an Internal Content Page – Top 10 Experiences – this incorporates address and contact details, photo and sub-text

Deliverable 7: The Membership Landing Page which should include:
1. Intro
2. Advertising & Sponsorship Space
3. The four sections
4. Tips Section
Updates

Hi all - just to reiterate that we are open to different approaches in the design.  We only included the existing screen shots of the beta site to provide you with an idea of the content.  We definitely don't want to see anything similar.....we want it to be edgy yet simple and easy to navigate....we want to create an outstanding user experience!  Cheers Tripvane Team

Reason: Dear Designers - We are extending the period as have not had many submissions at all and want to provide more time. If you have already submitted, we will be in touch shortly with feedback. Thanks for your understanding Tripvane Team

Reason: We would like to give everyone more time so we can find the best and most preferred design.

Target Market(s)

TARGET MARKET
tripvane is a consumer focused website, offering a wide-range of easy-to-use and interactive platforms, for informative and commercial purposes, while also providing attractive and innovative advertising real-estate for potential business partners.

The target audience can be segmented as follows:

Primary Target: Professionals travelling on Business

They require up-to-date reliable information prior and during their travel, as well as facilitation to take action. They need an online Personal Assistant.

The personal characteristics of the primary target group are: busy life, tailored solutions, reliable sources, trusting, caring, and spoiled.
 
The website will have a membership option (for a small annual fee) which will provide customized information for their demographic and preferences. Sub target groups will include:
1. Business Men 40 years
3. Business Women 40 years
5. Business People with reduced mobility

Demographic & Travelling Profile of Business Travellers

• 92% of them use the internet as a source of info
• 54% are males, 38 years old
• 80% holds a college/university degree
• 68% is travelling mainly for leisure and annually 6 times per year
• 52% reserve their ticket through the internet
• 66% is travel internationally

Secondary Targets:

Executive PA’s
Executive personal assistants who need to plan their manager’s travel and provide support information for their trip.

Professionals travelling for Leisure and Partners
They have most probably used the website for their business travel, but consider it also useful for their leisure travel. The generic website, will include enough information to cover most of the leisure needs, as well as the requirements of their partners.

Direct Business-to-Business [B2B] Targets
The direct [B2B] targeted audience includes corporations that would like to use a white label solution for their staff, by using all available destinations or a selected number depending on their global network.

Business-to-Business [B2B] Targets
The [B2B] targeted audience is an indirect audience, for which tripvane promotes its services, and a key revenue stream. The B2B audience consists mainly of a diverse range of professional organisations targeting the business traveller (airlines, hotels, travel agencies, tourism authorities, entertainment companies, services, etc.) tripvane will be targeting these organisations to advertise on the site.
 
Desired Response from Target Groups

The desired response from the consumer targets is:
a) Recurrent use of website
b) Share content/experience with friends and social networking sites
c) Interact on the website’s Blog
d) Register for newsletters and offers
e) Subscribe to Membership
f) Be exposed to commercial advertisements on the website
g) Provide feedback (in the future) for services
h) Use (in the future) online services to purchase products and services
Competition

Industry/Entity Type

Travel

Requirements
Must have
• A clean crisp and professional appearance giving a sense of Trust and Reliability.
Should not have
• It should not look like every other run of the mill travel sites - Roomly.com, Wanderpost etc

```html
<!DOCTYPE html>
<html lang="en">
<head>
<meta charset="utf-8">
<title>tripvane – Dubai City Guide</title>
<link rel="stylesheet" href="https://fonts.googleapis.com/css2?family=Lato:wght@300;400;700&display=swap">
<style>
:root{
  --orange:#f07c12;
  --orange-dark:#e26c08;
  --grey-dark:#3f3f3f;
  --grey-mid:#4d4d4d;
  --text:#333;
  --muted:#666;
  --white:#fff;
  --line:#ddd;
}
*{box-sizing:border-box;margin:0;padding:0}
html,body{width:1200px;height:786px;overflow:hidden;background:var(--white);font-family:'Lato',sans-serif;color:var(--text)}
.page{position:relative;width:1200px;height:786px}

/* header */
.site-header{position:absolute;left:0;top:0;width:1200px;height:73px;box-shadow:0 8px 14px -10px rgba(0,0,0,.12)}
.brand{position:absolute;left:200px;top:19px;display:flex;align-items:center;gap:10px}
.brand-mark{width:38px;height:38px;background:var(--grey-dark)}
.brand-name{font-size:36px;font-weight:700;color:var(--orange);letter-spacing:-1px;line-height:38px}
.main-nav{position:absolute;left:546px;top:30px;display:flex;gap:21px;font-size:13.5px;color:#555}
.btn{position:absolute;top:23px;height:29px;width:87px;color:#fff;font-size:13px;font-weight:700;display:flex;align-items:center;justify-content:center;letter-spacing:-.2px}
.btn-login{left:819px;background:var(--grey-mid)}
.btn-signup{left:914px;background:var(--orange)}

/* tiles */
.tile{position:absolute;color:#fff}
.tile-search{left:200px;top:94px;width:119px;height:119px;background:var(--grey-mid);text-align:center}
.tile-search svg{position:absolute;left:35px;top:24px}
.tile-label{position:absolute;left:0;right:0;top:86px;font-size:16px;text-align:center}
.tile-city{left:328px;top:94px;width:120px;height:119px;background:linear-gradient(180deg,#5a5a8a 0%,#3a3358 55%,#1e1a2a 100%)}
.tile-city svg{position:absolute;left:33px;top:22px}
.tile-weather{left:457px;top:94px;width:285px;height:119px;background:var(--grey-mid)}
.tile-weather svg{position:absolute;left:28px;top:29px}
.temp{position:absolute;left:131px;top:28px;font-size:54px;font-weight:300;letter-spacing:-3px}
.photo-tall{left:752px;top:94px;width:120px;height:248px;background:linear-gradient(180deg,#3d5fa8 0%,#6b7fc2 45%,#8a90c4 75%,#6f6a86 100%)}
.tile-clock{left:881px;top:94px;width:120px;height:119px;background:var(--orange)}
.clock-time{position:absolute;right:14px;top:24px;font-size:46px;font-weight:300;letter-spacing:-3px;line-height:50px}
.clock-ampm{position:absolute;right:22px;top:68px;font-size:18px;font-weight:300}
.photo-small{left:881px;top:222px;width:120px;height:120px;background:linear-gradient(160deg,#9ec3ee 0%,#4f7fc8 50%,#2d58a8 100%)}

/* journey */
.journey{position:absolute;left:200px;top:222px;width:542px;height:120px;background:var(--orange);overflow:hidden}
.journey h2{position:absolute;left:17px;top:12px;font-size:30px;font-weight:300;color:var(--grey-dark);letter-spacing:-1.3px}
.field-label{position:absolute;top:47px;font-size:13px;color:#fff}
.field{position:absolute;top:67px;height:34px;background:#fff;font-size:13px;color:#555;padding-left:8px;display:flex;align-items:center;white-space:nowrap}
.field.select::after{content:"";position:absolute;right:12px;top:15px;border-left:6px solid transparent;border-right:6px solid transparent;border-top:6px solid #aaa}
.f-amount{left:19px;width:75px}
.f-from{left:101px;width:157px}
.f-to{left:267px;width:157px}
.f-rate{left:431px;width:75px}
.l-from{left:101px}
.l-to{left:267px}

/* overview */
.overview{position:absolute;left:200px;top:354px;width:800px}
.overview h1{display:inline-block;font-size:32px;font-weight:300;color:var(--orange);letter-spacing:-1px;vertical-align:baseline}
.overview .place{display:inline-block;margin-left:12px;font-size:16px;color:var(--text)}
.overview p{margin-top:7px;padding-left:2px;width:782px;font-size:13px;line-height:15.3px;color:#444}
.read-more{display:block;margin-top:5px;padding-left:2px;font-size:13px;font-weight:700;color:var(--text);letter-spacing:-.3px}

/* directory panel */
.directory{position:absolute;left:200px;top:494px;width:801px;height:215px;background:linear-gradient(180deg,#5b5b5b 0%,#3c3c3c 100%);color:#fff}
.dir-col{position:absolute;top:24px}
.dir-col h3{font-size:21px;font-weight:400;letter-spacing:-.8px;margin-bottom:10px;white-space:nowrap}
.dir-col ul{list-style:none}
.dir-col li{position:relative;font-size:12px;line-height:19px;padding-left:16px;white-space:nowrap}
.dir-col li::before{content:"";position:absolute;left:2px;top:6px;width:7px;height:7px;background:#fff;border-radius:1px}

/* footer */
.site-footer{position:absolute;left:0;top:729px;width:1200px;border-top:1px solid var(--line);height:57px;font-size:11px;color:var(--muted)}
.copyright{position:absolute;left:200px;top:20px}
.social{position:absolute;left:483px;top:20px;display:flex;gap:14px}
.social span{width:12px;height:12px;border-radius:50%;background:#999}
.footer-nav{position:absolute;right:199px;top:20px;display:flex;gap:8px}
.footer-nav .sep{color:#999}
</style>
</head>
<body>
<div class="page">

<header class="site-header">
  <div class="brand"><span class="brand-mark"></span><span class="brand-name">tripvane</span></div>
  <nav class="main-nav"><span>General</span><span>Business</span><span>Leisure</span><span>Personal</span></nav>
  <span class="btn btn-login">LOGIN</span>
  <span class="btn btn-signup">SIGN UP</span>
</header>

<section class="tile tile-search">
  <svg width="50" height="50" viewBox="0 0 50 50"><circle cx="20" cy="20" r="14" fill="none" stroke="#fff" stroke-width="7"/><line x1="30" y1="30" x2="44" y2="44" stroke="#fff" stroke-width="8" stroke-linecap="round"/></svg>
  <span class="tile-label">Search</span>
</section>

<section class="tile tile-city" role="img" aria-label="Night skyline of a city with a lit tower">
  <svg width="54" height="54" viewBox="0 0 54 54"><circle cx="27" cy="27" r="23" fill="none" stroke="#fff" stroke-width="5"/><polygon points="35,19 29,29 25,25" fill="#fff"/><polygon points="19,35 25,25 29,29" fill="#fff" opacity=".7"/></svg>
  <span class="tile-label">DUBAI</span>
</section>

<section class="tile tile-weather">
  <svg width="80" height="56" viewBox="0 0 80 56"><circle cx="24" cy="22" r="10" fill="none" stroke="#f07c12" stroke-width="3"/><g stroke="#f07c12" stroke-width="3" stroke-linecap="round"><line x1="24" y1="2" x2="24" y2="6"/><line x1="4" y1="22" x2="8" y2="22"/><line x1="10" y1="8" x2="13" y2="11"/><line x1="38" y1="8" x2="35" y2="11"/><line x1="10" y1="36" x2="13" y2="33"/></g><path d="M18 54 a10 10 0 0 1 0-20 a14 14 0 0 1 27-6 a12 12 0 0 1 22 6 a10 10 0 0 1 1 20 z" fill="#f07c12"/></svg>
  <span class="temp">36°C</span>
</section>

<div class="tile photo-tall" role="img" aria-label="Sail-shaped hotel tower against a blue sky"></div>

<section class="tile tile-clock">
  <span class="clock-time">2:33</span>
  <span class="clock-ampm">PM</span>
</section>

<div class="tile photo-small" role="img" aria-label="Looking up at a very tall glass skyscraper"></div>

<section class="journey">
  <h2>Start your journey</h2>
  <span class="field-label l-from">From:</span>
  <span class="field-label l-to">To:</span>
  <span class="field f-amount">100</span>
  <span class="field select f-from">United Arab Emirates</span>
  <span class="field select f-to">America</span>
  <span class="field f-rate">27.22</span>
</section>

<section class="overview">
  <h1>City Overview</h1><span class="place">Dubai, United Arab Emirates</span>
  <p>Lorem ipsum dolor sit amet, consectetuer adipiscing elit, sed diam nonummy nibh euismod tincidunt ut laoreet dolore magna aliquam erat volutpat. Ut wisi enim ad minim veniam, quis nostrud exerci tation ullamcorper suscipit lobortis nisl ut aliquip ex ea commodo consequat. Duis autem vel eum iriure dolor in hendrerit in vulputate velit esse molestie consequat, vel illum dolore eu feugiat nulla facilisis at vero eros et accumsan et ...</p>
  <span class="read-more">Read More</span>
</section>

<section class="directory">
  <div class="dir-col" style="left:37px">
    <h3>General Information</h3>
    <ul><li>City Overview</li><li>Embassies &amp; Consulates</li><li>Fast Facts</li><li>Health &amp; Safety</li><li>Immigration &amp; Visas</li><li>Maps</li><li>Weather</li></ul>
  </div>
  <div class="dir-col" style="left:241px">
    <h3>People &amp; Culture</h3>
    <ul><li>Etiquette</li><li>History &amp; Culture</li><li>Holidays &amp; Festivals</li><li>Language &amp; Phases</li><li>Photo Gallery</li><li>Suburbs &amp; Areas</li></ul>
  </div>
  <div class="dir-col" style="left:419px">
    <h3>Accommodation</h3>
    <ul><li>Bed &amp; Breakfasts</li><li>Boarding Hostels</li><li>Hotels</li><li>Motels</li><li>Serviced Apartments</li><li>Vacation Rentals</li></ul>
  </div>
  <div class="dir-col" style="left:591px">
    <h3>Travel &amp; Transportation</h3>
    <ul><li>Airlines</li><li>Airports</li><li>Car Hire &amp; Limo’s</li><li>Ferries &amp; Ships</li><li>Ports &amp; Harbours</li><li>Public Transportation</li></ul>
  </div>
</section>

<footer class="site-footer">
  <span class="copyright">© 2013 Tripvane.com &nbsp;&nbsp;All rights reserved.</span>
  <div class="social" aria-label="Social links"><span></span><span></span><span></span><span></span><span></span></div>
  <nav class="footer-nav"><span>Blog</span><span class="sep">|</span><span>Privacy Policy</span><span class="sep">|</span><span>Terms &amp; Conditions</span><span class="sep">|</span><span>Jobs</span><span class="sep">|</span><span>Contact Us</span></nav>
</footer>

</div>
</body>
</html>
```